Open Now Poster for Retail Shop windows.

To design a poster to be printed to put on the windows of our retail stores to tell customers that we are open. Size is to be 590mm W x 840mm H supplied as a pdf. Design should incorporate our logo as well as other elements which indicate the style of our shop which is Womens Beach, Resort & Casual Clothing, Swimwear and Accessories. I would like the design to incorporate the words "Open Now" in some form in large lettering. I would also like the poster to be timeless and able to be used for other wording, so no images would be preferable.

Target Market(s)

Womens Beach, Resort & Casual Clothing, Swimwear and Accessories

Industry/Entity Type

Retail

Colors
e34297

Requirements
Must have
• words "Open Now". as well as our logo.

```html
<!DOCTYPE html>
<html lang="en">
<head>
<meta charset="utf-8">
<title>Sea Belle – Open Now</title>
<link rel="stylesheet" href="https://fonts.googleapis.com/css2?family=Montserrat:wght@700;900&display=swap">
<style>
  :root {
    --brand-pink: #e34297;
    --pink-light: #ea5ea6;
    --frond-dark: #3a1420;
    --shadow-plum: #4a0b2c;
    --gold: #d9a652;
    --gold-light: #f1d58e;
    --gold-deep: #c1892f;
    --paper: #ffffff;
  }
  html, body {
    margin: 0;
    padding: 0;
    overflow: hidden;
    background: var(--paper);
  }
  .poster {
    position: relative;
    width: 843px;
    height: 1200px;
    overflow: hidden;
    background: var(--paper);
    font-family: "Montserrat", Arial, sans-serif;
  }
  .side-band {
    position: absolute;
    top: 0;
    width: 87px;
    height: 1200px;
    background:
      linear-gradient(160deg, transparent 0 30%, rgba(58,20,32,0.55) 30% 34%, transparent 34% 60%, rgba(58,20,32,0.5) 60% 64%, transparent 64%),
      linear-gradient(var(--brand-pink), var(--brand-pink));
  }
  .side-band--left { left: 0; }
  .side-band--right { right: 0; }
  .gold-rail {
    position: absolute;
    top: 0;
    width: 19px;
    height: 1200px;
    background: linear-gradient(180deg, var(--gold-light) 0%, var(--gold) 35%, var(--gold-deep) 62%, var(--gold-light) 100%);
  }
  .gold-rail--left { left: 106px; }
  .gold-rail--right { left: 718px; }
  .brand-name {
    position: absolute;
    top: 128px;
    left: 0;
    width: 843px;
    margin: 0;
    text-align: center;
    font-weight: 700;
    font-size: 66px;
    letter-spacing: -1px;
    color: var(--brand-pink);
  }
  .headline {
    position: absolute;
    top: 418px;
    left: 0;
    width: 843px;
    margin: 0;
    text-align: center;
    font-weight: 900;
    line-height: 0.86;
    color: var(--brand-pink);
    -webkit-text-stroke: 3px var(--gold-light);
    paint-order: stroke fill;
    text-shadow:
      2px 2px 0 var(--shadow-plum),
      4px 4px 0 var(--shadow-plum),
      6px 5px 0 var(--shadow-plum),
      8px 6px 0 var(--shadow-plum);
  }
  .headline__line { display: block; }
  .headline__line--open { font-size: 196px; letter-spacing: -4px; }
  .headline__line--now { font-size: 196px; letter-spacing: -2px; margin-top: 10px; }
  .wave {
    position: absolute;
    left: 0;
    bottom: 0;
    width: 843px;
    height: 360px;
  }
</style>
</head>
<body>
  <main class="poster">
    <div class="side-band side-band--left" role="img" aria-label="Dark palm frond silhouettes on pink"></div>
    <div class="side-band side-band--right" role="img" aria-label="Dark palm frond silhouettes on pink"></div>
    <div class="gold-rail gold-rail--left"></div>
    <div class="gold-rail gold-rail--right"></div>

    <p class="brand-name">sea belle</p>

    <h1 class="headline">
      <span class="headline__line headline__line--open">OPEN</span>
      <span class="headline__line headline__line--now">NOW</span>
    </h1>

    <svg class="wave" viewBox="0 0 843 360" aria-hidden="true">
      <path d="M756 205 C690 205 610 220 552 292 C610 250 690 250 756 275 Z" fill="var(--gold-light)" opacity="0.7"/>
      <path d="M843 190 L843 360 L700 360 C760 330 790 280 770 250 C730 230 640 240 552 290 C600 232 700 188 843 190 Z" fill="var(--brand-pink)"/>
      <path d="M0 230 C160 215 330 240 470 280 C600 315 700 310 780 290 L843 275 L843 360 L0 360 Z" fill="var(--gold-light)"/>
      <path d="M0 236 C160 222 330 246 470 286 C600 322 700 318 780 298 L843 282 L843 360 L0 360 Z" fill="var(--brand-pink)"/>
      <path d="M0 290 C200 270 380 300 520 330 C640 352 760 345 843 320 L843 360 L0 360 Z" fill="var(--pink-light)" opacity="0.6"/>
    </svg>
  </main>
</body>
</html>
```